MaxiPlano
Stationery / Business Cards
Professional
Ramiro Quesada
Engineering
Ave. Cerezos 284
Valle Verde
Ciudad Norte, Est.
MEXICO
01-800-MaxiPlano
ramiro.quesada@maxiplano.mx
www.maxiplano.mx

```html
<!DOCTYPE html>
<html lang="es">
<head>
<meta charset="utf-8">
<title>MaxiPlano — Stationery</title>
<link href="https://fonts.googleapis.com/css2?family=Montserrat:wght@400;600&display=swap" rel="stylesheet">
<style>
  :root{
    --brand-blue:#1e96d8;
    --brand-yellow:#f4d21f;
    --ink:#5a5a5a;
    --label:#8a8a8a;
    --rule:#d8d8d8;
    --paper:#ffffff;
    --canvas:#f7f7f7;
    --font:'Montserrat', Arial, sans-serif;
  }
  *{box-sizing:border-box;margin:0;padding:0}
  html,body{width:1200px;height:348px;overflow:hidden;background:var(--canvas);font-family:var(--font);color:var(--ink)}
  .sheet{position:relative;width:1200px;height:348px}
  .piece{position:absolute;background:var(--paper)}
  .framed{border:4px solid var(--brand-blue)}
  .caption{position:absolute;font-size:5px;color:var(--label);text-align:center;letter-spacing:.2px}
  .wordmark{position:absolute;color:var(--brand-blue);font-weight:600;white-space:nowrap;line-height:1}
  .contact{position:absolute;font-size:4px;line-height:5.5px;color:var(--ink);white-space:nowrap}
  .web{position:absolute;font-size:5px;letter-spacing:1.5px;color:var(--ink);white-space:nowrap}
  .flap{position:absolute;left:0;right:0}
</style>
</head>
<body>
<main class="sheet">

  <!-- Logo concept -->
  <div class="wordmark" style="left:40px;top:66px;font-size:13px">MaxiPlano</div>
  <div class="caption" style="left:36px;top:106px;width:110px">Logo Concept</div>

  <!-- Business card front -->
  <section class="piece framed" style="left:38px;top:130px;width:110px;height:55px;border-width:3px">
    <div class="wordmark" style="left:14px;top:20px;font-size:8px">MaxiPlano</div>
  </section>
  <div class="caption" style="left:38px;top:198px;width:110px">Business Card Front</div>

  <!-- Business card back -->
  <section class="piece framed" style="left:38px;top:220px;width:110px;height:60px;border-width:3px">
    <div class="contact" style="left:8px;top:8px;font-size:3.5px;line-height:5px">
      <strong>Ramiro Quesada</strong><br>Engineering<br>Ave. Cerezos 284, Valle Verde<br>Ciudad Norte, Est. MEXICO<br>01-800-MaxiPlano<br>ramiro.quesada@maxiplano.mx
    </div>
  </section>
  <div class="caption" style="left:38px;top:288px;width:110px">Business Card Back</div>

  <!-- Letterhead page 1 -->
  <section class="piece framed" style="left:152px;top:24px;width:224px;height:300px">
    <div class="wordmark" style="left:12px;top:12px;font-size:9px">MaxiPlano</div>
    <div class="contact" style="left:12px;bottom:14px">
      Ramiro Quesada<br>Ave. Cerezos 284<br>Valle Verde<br>Ciudad Norte, Est.<br>MEXICO<br>01-800-MaxiPlano<br>ramiro.quesada@maxiplano.mx<br>www.maxiplano.mx
    </div>
  </section>
  <div class="caption" style="left:152px;top:330px;width:224px">Letterhead Page 1</div>

  <!-- Letterhead page 2 -->
  <section class="piece framed" style="left:392px;top:24px;width:226px;height:300px">
    <div class="wordmark" style="left:12px;top:12px;font-size:9px">MaxiPlano</div>
    <div class="contact" style="left:0;right:0;bottom:14px;text-align:center">
      Ave. Cerezos 284, Valle Verde, Ciudad Norte, Est. MEXICO<br>01-800-MaxiPlano · www.maxiplano.mx
    </div>
  </section>
  <div class="caption" style="left:392px;top:330px;width:226px">Letterhead Page 2</div>

  <!-- Envelope front -->
  <section class="piece framed" style="left:632px;top:26px;width:232px;height:116px">
    <div class="wordmark" style="left:10px;top:10px;font-size:8px">MaxiPlano</div>
    <div class="contact" style="left:10px;top:22px;font-size:3.5px;line-height:5px">
      Ave. Cerezos 284<br>Valle Verde, Ciudad Norte, Est.<br>MEXICO
    </div>
  </section>
  <div class="caption" style="left:632px;top:150px;width:232px">Envelope Front</div>

  <!-- Envelope front, second size -->
  <section class="piece framed" style="left:632px;top:180px;width:232px;height:128px">
    <div class="wordmark" style="left:10px;top:10px;font-size:8px">MaxiPlano</div>
    <div class="contact" style="left:10px;top:22px;font-size:3.5px;line-height:5px">
      Ave. Cerezos 284<br>Valle Verde, Ciudad Norte, Est.<br>MEXICO
    </div>
  </section>
  <div class="caption" style="left:632px;top:316px;width:232px">Envelope Back</div>

  <!-- Envelope backs -->
  <section class="piece" style="left:900px;top:24px;width:252px;height:108px;border:1px solid var(--rule)">
    <div class="flap" style="top:0;height:72px;background:var(--brand-blue)"></div>
    <svg width="252" height="108" style="position:absolute;left:0;top:0" aria-hidden="true">
      <polyline points="0,108 126,72 252,108" fill="none" stroke="#d8d8d8" stroke-width="1"/>
    </svg>
    <span class="web" style="right:14px;top:80px">www.maxiplano.mx</span>
  </section>

  <section class="piece" style="left:900px;top:156px;width:252px;height:164px;border:1px solid var(--rule)">
    <div class="flap" style="top:0;height:60px;background:var(--brand-yellow)"></div>
    <span class="web" style="right:14px;top:68px">www.maxiplano.mx</span>
    <svg width="252" height="164" style="position:absolute;left:0;top:0" aria-hidden="true">
      <polyline points="0,86 110,126 142,126 252,86" fill="none" stroke="#d8d8d8" stroke-width="1"/>
      <line x1="0" y1="164" x2="110" y2="126" stroke="#d8d8d8" stroke-width="1"/>
      <line x1="252" y1="164" x2="142" y2="126" stroke="#d8d8d8" stroke-width="1"/>
    </svg>
  </section>
  <div class="caption" style="left:900px;top:328px;width:252px">Envelope Back Designs</div>

</main>
</body>
</html>
```